UNIVERSITY OF CASTERBROOK SAXOPHONE SENIOR RECITAL

I need a poster design for my senior saxophone recital. The title of it is "Hollow: a Voyage across the Width of Tone". My concept is completely contrasting to the idea of a typical university recital. I'm so put off by the idea of "clap..clap..{play some music}..clap..clap..repeat". My recital is all based off of sound. The music I selected is all very modern (i.e Piet Halvermuss 'Warm Past the Final Pour' for Saxophone and Coffee Machine). I've included the Gatherly link so you can see the picture I have in the background. I like the idea of minimal black and white photography. Also, I would like the time / date / location / etc. all included on it. Let your imaginations run wild! It's art for an artist!
https://www.gatherly.example/events/413920587716230/
Target Market(s)
University Students around the University of Casterbrook and locals around the art district of South Beach, FL.
Industry/Entity Type
University

```html
<!DOCTYPE html>
<html lang="en">
<head>
<meta charset="utf-8">
<title>Hollow: a Voyage across the Width of Tone — Recital Poster</title>
<link rel="stylesheet" href="https://fonts.googleapis.com/css2?family=Roboto+Condensed:wght@400;700&display=swap">
<style>
  :root {
    --stage: #3a3a3a;
    --ink: #000000;
    --paper: #ffffff;
    --panel: #2a2a2a;
    --panel-deep: #262626;
    --glow: #ff1a55;
    --glow-mid: #a0002a;
    --muted: #8a8a8a;
  }
  * { margin: 0; padding: 0; box-sizing: border-box; }
  html, body {
    width: 1200px;
    height: 1000px;
    overflow: hidden;
    background: var(--stage);
    font-family: "Roboto Condensed", "Arial Narrow", sans-serif;
  }
  .poster {
    position: absolute;
    left: 300px;
    top: 100px;
    width: 585px;
    height: 780px;
    overflow: hidden;
    background: var(--ink);
  }
  .poster-photo {
    position: absolute;
    inset: 0;
    background:
      radial-gradient(ellipse 210px 330px at 330px 420px, var(--glow) 0%, var(--glow-mid) 45%, rgba(60,0,15,0.6) 75%, rgba(0,0,0,0) 100%),
      linear-gradient(90deg, var(--ink) 0%, var(--ink) 100%);
  }
  .poster-art {
    position: absolute;
    inset: 0;
    width: 585px;
    height: 780px;
  }
  .title-main { font-weight: 700; fill: var(--paper); }
  .title-sub { font-weight: 400; fill: var(--paper); }
  .title-accent { font-weight: 400; fill: var(--ink); }
  .date-text { font-weight: 400; fill: var(--paper); }
  .date-day { font-weight: 700; fill: var(--paper); }

  .programme {
    position: absolute;
    left: 53px;
    top: 555px;
    color: var(--paper);
    font-size: 7.5px;
    line-height: 9px;
  }
  .programme-heading {
    display: block;
    width: 133px;
    background: var(--panel);
    font-weight: 700;
    font-size: 10px;
    line-height: 13px;
    margin-bottom: 4px;
  }
  .programme-sub {
    font-weight: 700;
    font-size: 8px;
    margin-top: 8px;
  }

  .event-link {
    position: absolute;
    left: 20px;
    top: 699px;
    display: flex;
    align-items: center;
    gap: 8px;
    color: var(--paper);
    font-weight: 700;
    font-size: 12px;
  }
  .event-link-mark {
    width: 32px;
    height: 32px;
    background: var(--muted);
    border-radius: 4px;
  }
  .footer-title {
    position: absolute;
    left: 22px;
    top: 744px;
    color: var(--paper);
    font-size: 11px;
    letter-spacing: 0.2px;
  }
  .footer-title strong { font-weight: 700; }
  .venue {
    position: absolute;
    right: 22px;
    top: 725px;
    text-align: right;
    color: var(--paper);
    font-size: 15px;
    line-height: 16px;
  }
</style>
</head>
<body>
  <main class="poster">
    <div class="poster-photo" role="img" aria-label="Black and red photograph: silhouette of a saxophonist in a hat playing against a red spotlight"></div>

    <svg class="poster-art" viewBox="0 0 585 780" xmlns="http://www.w3.org/2000/svg">
      <!-- footer band -->
      <polygon fill="var(--panel-deep)" points="0,721 585,669 585,780 0,780"/>

      <!-- title block -->
      <g class="title" transform="translate(76 244) rotate(-20)">
        <polygon fill="var(--paper)" points="450,-8 820,-8 820,96 318,96 318,44 450,44"/>
        <text class="title-main" x="0" y="0" font-size="128" textLength="400" lengthAdjust="spacingAndGlyphs">HOLLOW</text>
        <text class="title-sub" x="175" y="34" font-size="38" textLength="265" lengthAdjust="spacingAndGlyphs">A VOYAGE ACROSS</text>
        <text class="title-sub" x="12" y="86" font-size="50" textLength="298" lengthAdjust="spacingAndGlyphs">THE WIDTH OF</text>
        <text class="title-accent" x="328" y="86" font-size="50" textLength="118" lengthAdjust="spacingAndGlyphs">TONE</text>
      </g>

      <!-- date panel -->
      <polygon fill="var(--paper)" points="0,383 228,323 246,498 0,556"/>
      <polygon fill="var(--panel)" points="0,389 236,339 245,500 0,549"/>
      <g class="date" transform="rotate(-8 120 460)">
        <text class="date-text" x="18" y="446" font-size="33" textLength="150" lengthAdjust="spacingAndGlyphs">DECEMBER</text>
        <text class="date-text" x="175" y="474" font-size="33" text-anchor="end">2013</text>
        <text class="date-day" x="178" y="476" font-size="86">8</text>
        <line x1="24" y1="490" x2="232" y2="490" stroke="var(--paper)" stroke-width="2"/>
        <text class="date-text" x="232" y="530" font-size="44" text-anchor="end">2PM</text>
      </g>
    </svg>

    <section class="programme">
      <span class="programme-heading">WORKS BY</span>
      <div>Lorenzo Vatterini</div>
      <div>Dr. Martin Holloway *WORLD PREMIERE*</div>
      <div>Piet Halvermuss</div>
      <div>Dr. Eleanor Pratchett*WORLD PREMIERE*</div>
      <div>Samuel Brooke</div>
      <div class="programme-sub">INTERMISSION</div>
      <div>Walter Greave</div>
    </section>

    <div class="event-link">
      <span class="event-link-mark"></span>
      <span>GATHERLY</span>
    </div>
    <p class="footer-title"><strong>HOLLOW</strong>: A VOYAGE ACROSS THE WIDTH OF TONE</p>

    <address class="venue" style="font-style: normal;">
      ADRIAN M. FOSS RECITAL HALL<br>
      MARLOW BAY, FLORIDA 33990
    </address>
  </main>
</body>
</html>
```